Email Design Creative Design Needed

Our website is called CampusLedger.org. One of our competitor(varsity scout.us.com) is using the following email creative.
http://qtr.brightvelmo.com/Affiliate/Assets/3532.html
http://qtr.brightvelmo.com/Affiliate/Assets/7921.html
http://qtr.brightvelmo.com/Affiliate/Assets/8061.html

We would like to use similar email creative without copying their exact creative. You can use the above as a guide but then come up with your own version of the creative.
The above are just concepts, please be creative and come up with your own version of it, without feeling that they have been copied. Feel free to move the components around. Also, feel free to change the colours and text.

Please find attached the CampusLedger.org logo.

Reason: We would like to receive more designs.

Industry/Entity Type

College

```html
<!DOCTYPE html>
<html lang="en">
<head>
<meta charset="utf-8">
<title>CampusLedger.org – Career Programs Email</title>
<link rel="stylesheet" href="https://fonts.googleapis.com/css2?family=Ubuntu:wght@400;500&family=Arimo:wght@400&display=swap">
<style>
  :root {
    --lime: #d6cf3a;
    --lime-light: #e3db5c;
    --forest: #4c6b2a;
    --body-yellow: #dcd34c;
    --panel: #efe9a2;
    --rule: #b9ad45;
    --magenta: #8e1d62;
    --magenta-light: #b0407f;
    --magenta-dark: #5e0f40;
    --pale-green: #cfe79a;
    --arrow-green: #8cc63f;
    --text-green: #4b8a2b;
    --link-red: #c8462a;
    --logo-grey: #6d6d6d;
    --ink: #222222;
    --white: #ffffff;
  }
  * { box-sizing: border-box; margin: 0; padding: 0; }
  html, body { width: 985px; height: 1200px; overflow: hidden; background: var(--white); }
  body { position: relative; font-family: "Arimo", Arial, sans-serif; }

  .top-bar { position: absolute; left: 123px; top: 0; width: 739px; height: 16px; display: flex; }
  .top-bar span { display: block; height: 100%; }
  .top-bar .edge { width: 22px; background: var(--forest); }
  .top-bar .lime { width: 347px; background: var(--lime); }
  .top-bar .forest { flex: 1; background: var(--forest); }

  .header { position: absolute; left: 123px; top: 16px; width: 739px; height: 113px;
    background: linear-gradient(#ffffff, #f1f1f1); border-bottom: 1px solid #c9c9c9; }
  .brand { position: absolute; left: 37px; top: 41px; display: flex; align-items: center; gap: 9px; }
  .brand-dot { width: 32px; height: 32px; border-radius: 50%; background: var(--lime); }
  .brand-name { font-family: "Ubuntu", sans-serif; font-weight: 500; font-size: 33px; color: var(--logo-grey); letter-spacing: -0.3px; }
  .header-photo { position: absolute; right: 0; top: 0; width: 370px; height: 112px;
    background: linear-gradient(100deg, rgba(255,255,255,1) 0%, #e6e6e2 30%, #d4d3cc 70%, #bdbcb3 100%); }

  .body-area { position: absolute; left: 123px; top: 129px; width: 739px; height: 899px;
    background: radial-gradient(ellipse 70% 40% at 50% 92%, #f2ec9a 0%, var(--body-yellow) 70%); }

  .hero { position: absolute; left: 142px; top: 149px; width: 703px; height: 374px;
    border-radius: 18px; border: 1px solid #3c4a22; overflow: hidden;
    background: linear-gradient(90deg, #8a8e92 0%, #6f7d6a 35%, #5b8a3c 60%, #5a9140 100%); }
  .hero-photo { position: absolute; inset: 0; }
  .hero-headline { position: absolute; right: 48px; top: 62px; text-align: right;
    font-family: "Ubuntu", sans-serif; font-size: 31px; line-height: 37px; color: var(--white); }

  .cta { position: absolute; left: 574px; top: 387px; width: 301px; height: 76px; text-decoration: none; }
  .cta-body { position: absolute; inset: 0; border-radius: 38px 0 0 38px;
    background: linear-gradient(var(--magenta-light), var(--magenta) 55%, var(--magenta-dark));
    box-shadow: 0 2px 3px rgba(0,0,0,0.3); }
  .cta-label { position: absolute; left: 36px; top: 14px; font-family: "Ubuntu", sans-serif;
    font-size: 21px; line-height: 24px; color: var(--pale-green); }
  .cta-divider { position: absolute; left: 162px; top: 4px; width: 1px; height: 68px; background: rgba(255,255,255,0.3); }
  .cta-icon { position: absolute; left: 185px; top: 20px; }
  .cta-fold { position: absolute; left: 860px; top: 463px; }

  .table-band { position: absolute; left: 110px; top: 533px; width: 767px; height: 58px;
    background: linear-gradient(var(--magenta-light), var(--magenta) 60%, var(--magenta-dark));
    display: flex; }
  .table-band div { display: flex; align-items: center; justify-content: center;
    font-family: "Ubuntu", sans-serif; font-size: 18px; color: var(--white); }
  .table-band .col-occ { width: 265px; border-right: 1px solid rgba(255,255,255,0.25); }
  .table-band .col-sal { width: 234px; border-right: 1px solid rgba(255,255,255,0.25); }
  .table-band .col-next { flex: 1; }
  .band-fold { position: absolute; top: 591px; }

  .salary-panel { position: absolute; left: 142px; top: 601px; width: 700px; height: 346px;
    border-radius: 14px; background: var(--panel); padding: 0 17px 0 14px; }
  .salary-row { display: grid; grid-template-columns: 208px 232px 1fr; align-items: center;
    border-bottom: 1px solid var(--rule); font-size: 13.5px; line-height: 16px; color: var(--text-green); text-align: center; }
  .salary-row:last-child { border-bottom: none; }
  .salary-row:nth-child(1) { height: 72px; }
  .salary-row:nth-child(2) { height: 71px; }
  .salary-row:nth-child(3) { height: 67px; }
  .salary-row:nth-child(4), .salary-row:nth-child(5) { height: 68px; }
  .program-link { color: var(--link-red); text-decoration: underline; }

  .footnote { position: absolute; left: 123px; top: 959px; width: 739px; text-align: center; font-size: 10px; color: var(--ink); }

  .legal { position: absolute; left: 156px; top: 1050px; width: 669px; text-align: center;
    font-size: 10.5px; line-height: 12.5px; color: var(--ink); }
  .legal p + p { margin-top: 12px; }
  .legal-rule { position: absolute; left: 156px; top: 1153px; width: 669px; height: 1px; background: #8a8a8a; }
  .rights { position: absolute; left: 156px; top: 1161px; width: 669px; text-align: center; font-size: 10.5px; color: var(--ink); }
</style>
</head>
<body>
  <div class="top-bar"><span class="edge"></span><span class="lime"></span><span class="forest"></span></div>

  <header class="header">
    <div class="brand"><span class="brand-dot"></span><span class="brand-name">CampusLedger.org</span></div>
    <div class="header-photo" role="img" aria-label="Photo of an open textbook lying on a desk"></div>
  </header>

  <div class="body-area"></div>

  <section class="hero">
    <div class="hero-photo" role="img" aria-label="Photo of a student studying at a desk, fading into a green overlay"></div>
    <h1 class="hero-headline" style="font-weight:400">Lorem ipsum dolor sit<br>amet, consectetur<br>adipisicing elit</h1>
  </section>

  <a class="cta" href="#">
    <span class="cta-body"></span>
    <span class="cta-label">Learn More<br>About Us</span>
    <span class="cta-divider"></span>
    <svg class="cta-icon" width="36" height="36" viewBox="0 0 36 36" aria-hidden="true">
      <circle cx="18" cy="18" r="17" fill="var(--arrow-green)"/>
      <path d="M9 14.5h10v-5l9 8.5-9 8.5v-5H9z" fill="#2f5a14"/>
    </svg>
  </a>
  <svg class="cta-fold" width="15" height="12" viewBox="0 0 15 12" aria-hidden="true"><path d="M0 0h15L0 12z" fill="var(--magenta-dark)"/></svg>

  <div class="table-band">
    <div class="col-occ">Occupation Type</div>
    <div class="col-sal">Median Salary</div>
    <div class="col-next">Next Steps</div>
  </div>
  <svg class="band-fold" style="left:110px" width="13" height="12" viewBox="0 0 13 12" aria-hidden="true"><path d="M0 0h13v12z" fill="var(--magenta-dark)"/></svg>
  <svg class="band-fold" style="left:862px" width="15" height="12" viewBox="0 0 15 12" aria-hidden="true"><path d="M0 0h15L0 12z" fill="var(--magenta-dark)"/></svg>

  <section class="salary-panel">
    <div class="salary-row">
      <span>Preschool and Childcare<br>Center/Program Get Started</span>
      <span>$41,030 per year*</span>
      <a class="program-link" href="#">Substance Abuse and Behavioral<br>Disorder Counselors Programs</a>
    </div>
    <div class="salary-row">
      <span>Education Administrators<br>Get Started</span>
      <span>$41,030 per year*</span>
      <a class="program-link" href="#">Substance Abuse and Behavioral<br>Disorder Counselors Programs</a>
    </div>
    <div class="salary-row">
      <span>Elementary and Secondary School<br>Get Started</span>
      <span>$41,030 per year*</span>
      <a class="program-link" href="#">Substance Abuse and Behavioral<br>Disorder Counselors Programs</a>
    </div>
    <div class="salary-row">
      <span>Educational, Guidance, School,<br>and Vocational Counselors<br>Get Started</span>
      <span>$41,030 per year*</span>
      <a class="program-link" href="#">Substance Abuse and Behavioral<br>Disorder Counselors Programs</a>
    </div>
    <div class="salary-row">
      <span>Preschool Teachers Get Started</span>
      <span>$41,030 per year*</span>
      <a class="program-link" href="#">Substance Abuse and Behavioral<br>Disorder Counselors Programs</a>
    </div>
  </section>

  <p class="footnote">*Median salaries according to the U.S. Bureau of Labor Statistics</p>

  <footer>
    <div class="legal">
      <p>Disclaimer:*Financial Aid is available for those who qualify. To see if you qualify for financial aid of any kind you must speak<br>with a representative of one of our partnering schools.</p>
      <p>Program outcomes vary according to each institution’s specific curriculum, and employment opportunities are not guaranteed.</p>
      <p>We hope you enjoyed receiving this email. Should you no longer wish to receive emails from this company visit this link<br>to unsubscribe or mail us at Brightvelmo Outreach Inc PO Box 410027 #52190 Riverton, IL 60999-0027</p>
    </div>
    <div class="legal-rule"></div>
    <p class="rights">All Rights Reserved.</p>
  </footer>
</body>
</html>
```